Potential SF Gazette Best Seller Poetry Book Cover Contest

I’m penning my first poetry book. It’s entitled “Lanterns Under Rain”
I’m fairly open to creative freedom but I want the cover to without a doubt catch a persons' eye instantly because first impressions are VERY IMPORTANT in the literary world
I tend to lean towards a luxury look and colors like black, gold, rose gold, silver, glitter etc but again I’m open to interpretation
Looking forward to your submissions
Target Market(s)
those seeking relatable love advice and quotes
modern millenials
Colors
Look and feel

```html
<!DOCTYPE html>
<html lang="en">
<head>
<meta charset="utf-8">
<title>Lanterns Under Rain — Poetry Book Cover</title>
<link href="https://fonts.googleapis.com/css2?family=Jost:wght@900&family=Merienda:wght@400&display=swap" rel="stylesheet">
<style>
  :root {
    --ink-black: #020202;
    --satin-deep: #070707;
    --satin-shadow: #030303;
    --satin-mid: #1c1c1c;
    --satin-sheen: #4a4a4a;
    --satin-glint: #6a6a6a;
    --copper-dark: #2b1409;
    --copper-mid: #9c5b36;
    --copper-light: #e3a386;
    --copper-glow: #f0b8a0;
  }
  html, body {
    margin: 0;
    padding: 0;
    width: 829px;
    height: 1200px;
    overflow: hidden;
    background: var(--ink-black);
  }
  .cover {
    position: relative;
    width: 829px;
    height: 1200px;
    overflow: hidden;
    background: var(--satin-deep);
  }
  .satin-backdrop {
    position: absolute;
    inset: 0;
    background:
      linear-gradient(162deg, transparent 14%, rgba(90,90,90,.28) 18%, transparent 23%),
      linear-gradient(148deg, transparent 30%, rgba(80,80,80,.22) 34%, transparent 40%),
      linear-gradient(58deg, transparent 44%, rgba(105,105,105,.32) 49%, rgba(20,20,20,.2) 52%, transparent 56%),
      linear-gradient(70deg, transparent 60%, rgba(70,70,70,.25) 64%, transparent 69%),
      linear-gradient(20deg, transparent 64%, rgba(95,95,95,.3) 68%, transparent 73%),
      linear-gradient(120deg, transparent 72%, rgba(85,85,85,.26) 77%, transparent 82%),
      linear-gradient(172deg, transparent 78%, rgba(75,75,75,.3) 84%, transparent 90%),
      radial-gradient(ellipse 55% 10% at 25% 20%, rgba(120,120,120,.22), transparent 70%),
      radial-gradient(ellipse 30% 9% at 30% 55%, rgba(110,110,110,.2), transparent 70%),
      radial-gradient(ellipse 26% 7% at 52% 74%, rgba(150,150,150,.22), transparent 70%),
      radial-gradient(ellipse 40% 30% at 15% 88%, rgba(0,0,0,.7), transparent 70%),
      linear-gradient(150deg, #151515 0%, var(--satin-shadow) 38%, var(--satin-mid) 58%, var(--satin-shadow) 100%);
  }
  .satin-backdrop::after {
    content: "";
    position: absolute;
    inset: 0;
    background: radial-gradient(ellipse 90% 80% at 50% 50%, transparent 55%, rgba(0,0,0,.55) 100%);
  }
  .badge-band {
    position: absolute;
    left: 0;
    top: 27px;
    width: 100%;
    height: 59px;
    background: var(--ink-black);
    display: flex;
    align-items: center;
    justify-content: center;
  }
  .badge-text {
    margin: 0 0 0 20px;
    font-family: "Merienda", cursive;
    font-size: 35px;
    font-style: italic;
    letter-spacing: 0.5px;
    white-space: nowrap;
    color: var(--copper-mid);
    background: linear-gradient(90deg, var(--copper-mid), var(--copper-light) 50%, var(--copper-mid));
    -webkit-background-clip: text;
    background-clip: text;
    -webkit-text-fill-color: transparent;
  }
  .book-title {
    position: absolute;
    right: 48px;
    bottom: 40px;
    margin: 0;
    font-family: "Jost", sans-serif;
    font-weight: 900;
    font-size: 112px;
    line-height: 128px;
    text-align: center;
    text-transform: uppercase;
    letter-spacing: 1px;
  }
  .title-line {
    display: block;
    white-space: nowrap;
    background-clip: text;
    -webkit-background-clip: text;
    -webkit-text-fill-color: transparent;
    color: var(--copper-mid);
  }
  .title-line--first {
    background-image: linear-gradient(100deg, var(--copper-dark) 0%, var(--copper-dark) 25%, var(--copper-mid) 55%, var(--copper-light) 70%, var(--copper-mid) 85%, var(--copper-dark) 100%);
  }
  .title-line--second {
    background-image: linear-gradient(100deg, var(--copper-mid) 0%, var(--copper-light) 40%, var(--copper-mid) 75%, var(--copper-dark) 100%);
  }
  .title-line--third {
    background-image: linear-gradient(180deg, var(--copper-mid) 0%, var(--copper-glow) 100%);
  }
</style>
</head>
<body>
  <main class="cover">
    <div class="satin-backdrop" role="img" aria-label="Draped black satin fabric with deep diagonal folds and soft silver sheen"></div>
    <header class="badge-band">
      <p class="badge-text">SF Gazette Best Seller Poetry Book</p>
    </header>
    <h1 class="book-title">
      <span class="title-line title-line--first">Lanterns</span>
      <span class="title-line title-line--second">Under</span>
      <span class="title-line title-line--third">Rain</span>
    </h1>
  </main>
</body>
</html>
```